Real Estate Development Company Stationary

We need our company, business card, letterhead, pocket folder and envelope designed.

We are a new real estate development company. We focus on data centre, commercial and real estate development.

Please see attached for our logo. Since it's a new logo, you still can make minor adjust if you like it makes senses

The client has sent me a business card he really likes. Please see file 3.

Target Market(s)

Real Estate Investors
Large corporations
Home buyers

Industry/Entity Type

Real Estate

```html
<!DOCTYPE html>
<html lang="en">
<head>
<meta charset="utf-8">
<title>Keystone Development Inc. — Business Card</title>
<link rel="stylesheet" href="https://fonts.googleapis.com/css2?family=Didact+Gothic&family=Montserrat:wght@700&display=swap">
<style>
  :root {
    --navy: #123f7a;
    --green: #6cb33f;
    --paper: #ffffff;
    --ink: #4a4a4a;
    --rule: #b9bec6;
    --stage: #e9e9ed;
  }
  * { box-sizing: border-box; margin: 0; padding: 0; }
  html, body { width: 1200px; height: 934px; overflow: hidden; }
  body {
    background: var(--stage);
    font-family: "Didact Gothic", sans-serif;
    color: var(--ink);
    display: flex;
    align-items: center;
    justify-content: center;
    gap: 50px;
  }
  .card {
    position: relative;
    width: 525px;
    height: 300px;
    box-shadow: 0 6px 18px rgba(0,0,0,0.12);
  }
  .card--back { background: var(--navy); }
  .card--front { background: var(--paper); }

  .wordmark {
    position: absolute;
    display: flex;
    align-items: center;
    gap: 12px;
  }
  .wordmark__square { width: 26px; height: 26px; }
  .wordmark__name { font-size: 22px; line-height: 1; white-space: nowrap; }

  .card--back .wordmark { left: 70px; top: 134px; }
  .card--back .wordmark__square { background: var(--green); }
  .card--back .wordmark__name { color: #ffffff; }

  .card--front .wordmark { left: 40px; top: 118px; }
  .card--front .wordmark__square { background: var(--navy); }
  .card--front .wordmark__name { color: var(--green); }

  .holder {
    position: absolute;
    right: 38px;
    top: 34px;
    text-align: right;
  }
  .holder__name {
    font-family: "Montserrat", sans-serif;
    font-weight: 700;
    font-size: 17px;
    letter-spacing: 0.5px;
    color: var(--navy);
  }
  .holder__role { font-size: 14px; margin-top: 2px; }

  .contacts {
    position: absolute;
    left: 40px;
    right: 30px;
    bottom: 30px;
    display: flex;
    align-items: flex-end;
    font-size: 12.5px;
  }
  .contacts__group { display: flex; flex-direction: column; gap: 4px; padding: 0 16px; }
  .contacts__group:first-child { padding-left: 0; }
  .contacts__group + .contacts__group { border-left: 1px solid var(--rule); }
  .contacts__item { display: flex; align-items: center; gap: 7px; white-space: nowrap; }
  .icon { width: 13px; height: 13px; flex: none; }
</style>
</head>
<body>

<section class="card card--back" aria-label="Business card, back">
  <div class="wordmark">
    <span class="wordmark__square"></span>
    <span class="wordmark__name">Keystone Development Inc.</span>
  </div>
</section>

<section class="card card--front" aria-label="Business card, front">
  <div class="holder">
    <p class="holder__name">JORDAN HALE</p>
    <p class="holder__role">Manager</p>
  </div>

  <div class="wordmark">
    <span class="wordmark__square"></span>
    <span class="wordmark__name">Keystone Development Inc.</span>
  </div>

  <div class="contacts">
    <div class="contacts__group">
      <p class="contacts__item">
        <svg class="icon" viewBox="0 0 13 13" aria-hidden="true"><rect width="13" height="13" rx="2" fill="#6cb33f"/><rect x="4" y="2.5" width="5" height="8" rx="1" fill="none" stroke="#fff" stroke-width="1.2"/></svg>
        (07) 5210 4417
      </p>
      <p class="contacts__item">
        <svg class="icon" viewBox="0 0 13 13" aria-hidden="true"><rect width="13" height="13" rx="2" fill="#6cb33f"/><path d="M3 5.5h7v4H3z M4.5 5.5V3.5h4v2" fill="none" stroke="#fff" stroke-width="1.1"/></svg>
        (07) 5210 4490
      </p>
    </div>
    <div class="contacts__group">
      <p class="contacts__item">
        <svg class="icon" viewBox="0 0 13 13" aria-hidden="true"><rect width="13" height="13" rx="2" fill="#6cb33f"/><rect x="2.5" y="3.5" width="8" height="6" fill="none" stroke="#fff" stroke-width="1.1"/><path d="M2.5 3.5l4 3.2 4-3.2" fill="none" stroke="#fff" stroke-width="1.1"/></svg>
        hello@keystonedev.com
      </p>
      <p class="contacts__item">
        <svg class="icon" viewBox="0 0 13 13" aria-hidden="true"><rect width="13" height="13" rx="2" fill="#6cb33f"/><circle cx="6.5" cy="6.5" r="3.8" fill="none" stroke="#fff" stroke-width="1.1"/><path d="M2.7 6.5h7.6M6.5 2.7v7.6" stroke="#fff" stroke-width="1"/></svg>
        www.keystonedev.com
      </p>
    </div>
    <div class="contacts__group">
      <p class="contacts__item">Unit 9, 48 Harlow Street</p>
      <p class="contacts__item">Eastfield EF4 7QA</p>
    </div>
  </div>
</section>

</body>
</html>
```